Business Card and Letterhead for Nurlo - modern real estate business

I need a double sided business card design for Nurlo. Please see business card brief here https://papers.trelvimo.net/sheet/q/7XrTbaLeZpMmQ2uWvd9HkCj4yNoEfsGi3lRtAz_pk/view?mode=shared

Please feel free to design the business cards however you feel best. I am happy to give some creative freedoms and then provide feedback from there.

Please then also create a letterhead to match the business card design

Colors

Designer to choose colors to be used in the design.

Requirements
Must have
• Must be a modern, elegant business card which looks very professional

```html
<!DOCTYPE html>
<html lang="en">
<head>
<meta charset="utf-8">
<title>Nurlo Business Card</title>
<link href="https://fonts.googleapis.com/css2?family=Exo+2:wght@400;500;600&display=swap" rel="stylesheet">
<style>
  :root {
    --backdrop: #9b9b9b;
    --paper: #f7f7f7;
    --ink: #2a2a2a;
    --brand-red: #e01b24;
    --rule: #9a9a9a;
    --card-black: #121212;
    --photo-top: #8fa27a;
    --photo-bottom: #3a3d3f;
  }
  * { box-sizing: border-box; margin: 0; padding: 0; }
  html, body { width: 1200px; height: 969px; overflow: hidden; }
  body {
    background: var(--backdrop);
    font-family: "Exo 2", sans-serif;
    color: var(--ink);
    position: relative;
  }
  .card {
    position: absolute;
    left: 250px;
    width: 700px;
    height: 400px;
    border-bottom: 4px solid var(--brand-red);
    box-shadow: 0 14px 30px rgba(0,0,0,0.25);
  }
  .card-front { top: 60px; background: var(--paper); }
  .card-back {
    top: 510px;
    background: var(--card-black);
    display: flex;
    align-items: center;
    justify-content: center;
  }
  .agent-photo {
    position: absolute;
    left: 100px; top: 34px;
    width: 150px; height: 140px;
    border: 2px solid var(--brand-red);
    background: linear-gradient(160deg, var(--photo-top), var(--photo-bottom));
  }
  .agent-name {
    position: absolute;
    left: 92px; top: 182px;
    font-size: 26px; line-height: 32px; font-weight: 500;
    color: var(--brand-red);
    letter-spacing: 1px;
  }
  .agent-title {
    position: absolute;
    left: 88px; top: 216px;
    font-size: 15px; line-height: 20px; letter-spacing: 0.6px;
  }
  .divider {
    position: absolute;
    left: 80px; right: 60px; top: 262px;
    height: 1px; background: var(--rule);
  }
  .contact-list {
    position: absolute;
    list-style: none;
    font-size: 15px;
    letter-spacing: 0.6px;
    line-height: 24px;
  }
  .contact-list li { display: flex; align-items: center; gap: 8px; }
  .contact-list svg { width: 13px; height: 13px; flex: none; }
  .agent-contacts { left: 80px; top: 276px; }
  .agency-block {
    position: absolute;
    left: 520px; top: 130px;
  }
  .wordmark-small {
    font-size: 38px; line-height: 44px; font-weight: 600;
    color: var(--brand-red);
    letter-spacing: 3px;
    margin-bottom: 8px;
  }
  .agency-details { font-size: 15px; letter-spacing: 0.6px; line-height: 22px; }
  .agency-contacts { left: 500px; top: 276px; }
  .wordmark-large {
    font-size: 150px; font-weight: 600;
    color: var(--brand-red);
    letter-spacing: 10px;
  }
</style>
</head>
<body>
  <section class="card card-front">
    <div class="agent-photo" role="img" aria-label="Portrait photo of the agent outdoors"></div>
    <h1 class="agent-name">LIAM CARVER</h1>
    <p class="agent-title">Licenced Real Estate Agent</p>
    <div class="divider"></div>

    <ul class="contact-list agent-contacts">
      <li>Lic No. 20418826</li>
      <li>
        <svg viewBox="0 0 16 16"><path fill="var(--brand-red)" d="M3.6 1.5l2.3 2.8-1.3 1.6c.9 2 2.4 3.5 4.4 4.4l1.6-1.3 2.8 2.3-1.4 2.2C7 13.2 2.8 9 2.3 3z"/></svg>
        0412 583 907
      </li>
      <li>
        <svg viewBox="0 0 16 16"><rect x="1.5" y="3.5" width="13" height="9" fill="none" stroke="var(--brand-red)" stroke-width="1.4"/><path d="M1.5 3.5L8 9l6.5-5.5" fill="none" stroke="var(--brand-red)" stroke-width="1.4"/></svg>
        liam@nurlo.com
      </li>
    </ul>

    <div class="agency-block">
      <div class="wordmark-small">NURLO</div>
      <p class="agency-details">Lic No. 10372419<br>PO Box 1736<br>Larrow NSW 2790</p>
    </div>

    <ul class="contact-list agency-contacts">
      <li>
        <svg viewBox="0 0 16 16"><path fill="var(--brand-red)" d="M3.6 1.5l2.3 2.8-1.3 1.6c.9 2 2.4 3.5 4.4 4.4l1.6-1.3 2.8 2.3-1.4 2.2C7 13.2 2.8 9 2.3 3z"/></svg>
        02 4810 3359
      </li>
      <li>
        <svg viewBox="0 0 16 16"><rect x="1.5" y="3.5" width="13" height="9" fill="none" stroke="var(--brand-red)" stroke-width="1.4"/><path d="M1.5 3.5L8 9l6.5-5.5" fill="none" stroke="var(--brand-red)" stroke-width="1.4"/></svg>
        info@nurlo.com
      </li>
      <li>
        <svg viewBox="0 0 16 16"><g fill="none" stroke="var(--brand-red)" stroke-width="1.3"><circle cx="8" cy="8" r="6.3"/><ellipse cx="8" cy="8" rx="2.7" ry="6.3"/><path d="M1.7 8h12.6M2.8 4.8h10.4M2.8 11.2h10.4"/></g></svg>
        www.nurlo.com
      </li>
    </ul>
  </section>

  <section class="card card-back">
    <div class="wordmark-large">NURLO</div>
  </section>
</body>
</html>
```